Tampa Bay fishing guide needs stunning website.

I currently have a site - www.reelcoastcharters.example which I personally put together using the Plimo platform and I am looking for a redesign on a different platform (Sitebarn?) that will allow me to easily create landing pages in the future. Would like to have a block for visitors to opt in to newsletter. Need social media links on all pages.

I would like to let my visitors know that I am able to handle their fishing charter needs here in the Tampa Bay area, if I'm not available for the dates they are looking to go I can refer them to a reputable captain in the area.

Target Market(s)

United States

Industry/Entity Type

Tourism

Coding

Coded - Design and coding required

Number of Pages Required

5+ page

Font styles to use
Sans Serif

Colors
0355a3
3176b5
85abd2
fbf289

Requirements
Must have
• Mobile Responsive, Ability to insert Trackwise Metrics, Chatterly pixels, ability to add custom landing pages in future
Nice to have
• Clean, easy navigation

```html
<!DOCTYPE html>
<html lang="en">
<head>
<meta charset="utf-8">
<title>Marlow Charters – Tampa Bay Fishing Guide</title>
<link rel="stylesheet" href="https://fonts.googleapis.com/css2?family=Lato:wght@300;400;700;900&display=swap">
<style>
:root{
  --brand:#0355a3;
  --brand-mid:#3176b5;
  --brand-light:#85abd2;
  --accent:#fbf289;
  --ink:#0b1522;
  --night:#111a26;
  --navy:#061a33;
  --sky:#3a8fe4;
  --white:#ffffff;
  --muted:#c9d4e0;
}
*{box-sizing:border-box;margin:0;padding:0}
html,body{width:1200px;height:3156px;overflow:hidden}
body{font-family:"Lato",Arial,sans-serif;background:var(--ink);color:var(--white);position:relative}
a{color:inherit;text-decoration:none}

/* hero */
.hero{position:absolute;left:0;top:0;width:1200px;height:752px;overflow:hidden}
.hero-photo{position:absolute;inset:0;background:linear-gradient(120deg,#0f5e52 0%,#1f7d6a 35%,#2f6d78 60%,#a9b6b9 85%,#d6dbdc 100%)}
.hero-photo::after{content:"";position:absolute;inset:0;background:linear-gradient(180deg,rgba(0,0,0,.25),rgba(0,0,0,0) 30%,rgba(0,0,0,.2))}
.brand{position:absolute;display:flex;align-items:center;gap:12px;font-weight:900;color:var(--white)}
.brand-dot{border-radius:50%;background:var(--brand-light)}
.hero .brand{left:116px;top:36px;font-size:50px}
.hero .brand-dot{width:18px;height:18px}
.nav{position:absolute;right:96px;top:50px;display:flex;gap:10px;font-size:17px}
.nav a{padding:8px 16px;border-radius:4px}
.nav a.active{background:var(--white);color:var(--brand)}
.hero-title{position:absolute;left:120px;top:272px;width:520px;font-size:38px;line-height:48px;font-weight:700;text-shadow:0 2px 6px rgba(0,0,0,.5)}

/* intro */
.intro{position:absolute;left:0;top:752px;width:1200px;height:588px;background:radial-gradient(ellipse at center,#1b2533,#0d141d);text-align:center}
.intro h2{margin-top:86px;font-size:30px;font-weight:400;color:var(--sky)}
.avatar{width:160px;height:160px;border-radius:50%;margin:62px auto 0;background:linear-gradient(160deg,#7b8a96,#3d4c5a);border:5px solid var(--white)}
.caption{margin-top:22px;font-size:17px;color:var(--sky)}
.intro p{width:940px;margin:26px auto 0;font-size:15px;line-height:24px;color:var(--muted)}
.intro p+p{margin-top:18px}

/* services */
.services{position:absolute;left:0;top:1340px;width:1200px;height:540px}
.svc{position:absolute;top:0;height:540px;width:600px;text-align:center;padding-top:118px}
.svc-left{left:0;background:linear-gradient(180deg,#2c6db0,#1a4d85)}
.svc-right{left:600px;background:linear-gradient(180deg,#1d4d80,#12365d)}
.svc h3{font-size:40px;font-weight:700;line-height:48px}
.svc p{width:340px;margin:34px auto 0;font-size:14px;line-height:21px;color:#dce7f3}
.svc a{display:inline-block;margin-top:34px;font-size:14px;border-bottom:1px solid var(--white);padding-bottom:3px}
.wave{position:absolute;left:0;top:-1px;width:1200px;height:60px}
.seal{position:absolute;left:500px;top:86px;width:200px;height:200px;border-radius:50%;background:var(--white);border:6px solid var(--brand-light);display:flex;align-items:center;justify-content:center}
.seal .brand{position:static;font-size:38px;color:var(--brand)}
.seal .brand-dot{width:12px;height:12px;background:var(--brand)}

/* rates */
.rates{position:absolute;left:0;top:1880px;width:1200px;height:520px;background:radial-gradient(ellipse at center,#1b2533,#0d141d)}
.rates h2{text-align:center;margin-top:52px;font-size:36px;font-weight:400;color:var(--sky)}
.rates-rule{width:1000px;height:1px;background:#34506e;margin:22px auto 0}
.card{position:absolute;top:180px;width:340px;height:280px;border-radius:10px;overflow:hidden;background:linear-gradient(180deg,#1c5fa8,#0a3a72);text-align:center;box-shadow:0 6px 18px rgba(0,0,0,.5)}
.card-head{height:70px;line-height:70px;font-size:36px;font-weight:700;background:var(--brand-mid)}
.card .hours{margin-top:26px;font-size:20px}
.card .hours b{font-size:24px}
.card .price{margin-top:16px;font-size:17px;color:#dce7f3}
.card .btns{margin-top:26px;display:flex;justify-content:center;gap:14px}
.btn{display:inline-block;padding:8px 16px;border-radius:4px;background:var(--white);color:var(--brand);font-size:14px;font-weight:700}
.card-half{left:100px}
.card-full{left:760px}
.card-mid{left:420px;top:148px;width:360px;height:340px;z-index:2;background:linear-gradient(180deg,#0a4c96,#06305f)}
.card-mid .card-head{background:#cfe0f2;color:var(--brand);height:80px;line-height:80px}
.card-mid .hours{margin-top:40px}

/* quote & testimonials */
.contact{position:absolute;left:0;top:2400px;width:1200px;height:420px;background:linear-gradient(90deg,#0c2f57,#24518a 50%,#4f7fb5);overflow:hidden}
.contact-photo{position:absolute;inset:0;background:linear-gradient(180deg,rgba(255,255,255,.06),rgba(0,0,0,.25))}
.contact h2{position:absolute;top:34px;font-size:34px;font-weight:400}
.quote h2{left:100px}
.form{position:absolute;left:100px;top:112px;width:460px;display:grid;grid-template-columns:1fr 1fr;gap:14px}
.field{height:40px;background:var(--white);color:#7a8694;font-size:13px;padding:12px;border-radius:2px}
.field.wide{grid-column:1 / 3}
.field.msg{height:48px}
.send{grid-column:1 / 2;width:170px;height:44px;background:#d6dde5;color:#1b2a3a;font-size:20px;border-radius:2px;display:flex;align-items:center;justify-content:center}
.reviews h2{left:640px}
.review-box{position:absolute;left:640px;top:112px;width:460px;height:150px;background:var(--white);color:#3a4552;font-size:13px;line-height:20px;padding:18px 22px 18px 42px;font-style:italic}
.review-box::before{content:"\201C";position:absolute;left:14px;top:8px;font-size:38px;color:var(--brand)}
.reviewer{position:absolute;left:680px;top:270px;width:60px;height:60px;border-radius:50%;background:linear-gradient(160deg,#9aa7b2,#56626e);border:3px solid var(--white)}
.reviewer-name{position:absolute;left:800px;top:350px;font-size:13px;color:#e3ebf3}
.dots{position:absolute;left:820px;top:376px;display:flex;gap:8px}
.dots span{width:9px;height:9px;border-radius:50%;background:rgba(255,255,255,.5)}
.dots span:first-child{background:var(--white)}

/* footer */
.footer{position:absolute;left:0;top:2820px;width:1200px;height:292px;background:var(--navy)}
.col{position:absolute;top:30px}
.col h4{font-size:22px;font-weight:700}
.col h4 span{color:var(--sky)}
.links{left:100px}
.links ul{list-style:none;margin-top:20px;font-size:14px;line-height:25px;color:var(--muted)}
.links li::before{content:"› ";color:var(--sky)}
.badges{left:300px}
.badge-row{display:flex;gap:18px;margin-top:24px}
.badge{width:110px;height:90px;background:var(--white);border-radius:4px}
.badge+.badge{background:#e6f0d8}
.details{left:580px;width:320px}
.detail{display:flex;gap:12px;margin-top:20px;font-size:13px;line-height:19px;color:var(--muted)}
.detail svg{flex:none;width:18px;height:18px}
.footer .brand{left:930px;top:110px;font-size:42px}
.footer .brand-dot{width:14px;height:14px}
.copyright{position:absolute;left:0;top:3112px;width:1200px;height:44px;background:#030d1b;font-size:13px;color:#9aa8b7;display:flex;align-items:center;justify-content:space-between;padding:0 100px}
.follow{display:flex;align-items:center;gap:10px}
.follow span.ring{width:26px;height:26px;border-radius:50%;background:var(--brand-mid)}
</style>
</head>
<body>

<header class="hero">
  <div class="hero-photo" role="img" aria-label="Photo of anglers on a boat holding up a large snook caught on Tampa Bay"></div>
  <a class="brand" href="#"><span class="brand-dot"></span>Marlow</a>
  <nav class="nav">
    <a class="active" href="#">Home</a>
    <a href="#">About Us</a>
    <a href="#">Pick Up Locations</a>
    <a href="#">Rates</a>
    <a href="#">Contact Us</a>
    <a href="#">Gift Card</a>
  </nav>
  <h1 class="hero-title">Come Fish With Tampa Bay, FL Fishing Guide, Tampa Bay Fishing Charter Most Respected Captain, 25 Year Native Guide</h1>
</header>

<section class="intro">
  <h2>Tampa Bay, Fishing Guide, Tampa Bay Fishing Charters</h2>
  <div class="avatar" role="img" aria-label="Portrait photo of Capt. Dale Marlow"></div>
  <div class="caption">Capt. Dale Marlow, with over 20 years' experience</div>
  <p>Native Fishing Charter Tampa One Full And Half Day Fishing Charters On The Waters of Tampa Bay. If You're Looking For A Great Fishing Charter Tampa Don't Hesitate To Contact Capt. Dale Or You Can Simply Book Your Trip Online Here.</p>
  <p>Come Enjoy A Wonderful Day Fishing Charters Tampa For Tarpon, Snook, Redfish, Trout, Sharks, Cobia, Spanish Mackerel As Well As Others Aboard Capt. Dale Marlow Sport Fishing Charters Boat. Capt. Dale Will Work Hard To Ensure That You And Your Guests Have A Memorable Day Enjoying The Wonderful Game Fish That Tampa Bay Has To Offer.</p>
</section>

<section class="services">
  <div class="svc svc-left">
    <h3>Full &amp; Half Day<br>Charters</h3>
    <p>Offering Tampa Bay, FL Fishing Charters On The Beautiful Waters Of Tampa Bay. Fish With Capt. Dale Marlow, Tampa Bay FL Fishing Guide For Over 25 Years</p>
    <a href="#">Find Out More »</a>
  </div>
  <div class="svc svc-right">
    <h3>Multiple Pickup<br>Points</h3>
    <p>Whether you're looking for a fishing charter guide in Tampa, St. Pete, Clearwater or Bradenton, Capt. Dale can pick you up nearby. Click here for maps of pickup locations.</p>
    <a href="#">Maps &amp; Pickup Locations »</a>
  </div>
  <svg class="wave" viewBox="0 0 1200 60" preserveAspectRatio="none" aria-hidden="true">
    <path d="M0 0 H1200 V20 C1050 50 900 0 750 24 C600 48 450 4 300 26 C180 44 80 18 0 30 Z" fill="#0d141d"/>
  </svg>
  <div class="seal"><span class="brand"><span class="brand-dot"></span>Marlow</span></div>
</section>

<section class="rates">
  <h2>Our Rates</h2>
  <div class="rates-rule"></div>
  <div class="card card-half">
    <div class="card-head">Half Day</div>
    <div class="hours">(4 hour) <b>Charter</b></div>
    <div class="price">1-3 people $399</div>
    <div class="price">4 people $499</div>
    <div class="btns"><a class="btn" href="#">More Info</a><a class="btn" href="#">Get Started</a></div>
  </div>
  <div class="card card-mid">
    <div class="card-head">3/4 Day</div>
    <div class="hours">(6 hour) <b>Charter</b></div>
    <div class="price">1-3 people $499</div>
    <div class="price">4 people $599</div>
    <div class="btns"><a class="btn" href="#">More Info</a><a class="btn" href="#">Get Started</a></div>
  </div>
  <div class="card card-full">
    <div class="card-head">Full Day</div>
    <div class="hours">(8 hour) <b>Charter</b></div>
    <div class="price">1-3 people $599</div>
    <div class="price">4 people $699</div>
    <div class="btns"><a class="btn" href="#">More Info</a><a class="btn" href="#">Get Started</a></div>
  </div>
</section>

<section class="contact">
  <div class="contact-photo" role="img" aria-label="Photo of a fishing pier over calm bay water at dusk"></div>
  <div class="quote">
    <h2>Request A Quote</h2>
    <div class="form">
      <div class="field">First Name</div>
      <div class="field">Your Phone No</div>
      <div class="field wide">Your Email</div>
      <div class="field wide msg">Messages</div>
      <div class="send">Send Request</div>
    </div>
  </div>
  <div class="reviews">
    <h2>Client Testimonials</h2>
    <div class="review-box">Great day out with Capt. Dale on the bay. He knew every spot, kept the lines busy and had the kids landing redfish by mid morning. Friendly, patient and safe the whole trip. We have already booked again for next spring and cannot wait to get back out there.</div>
    <div class="reviewer" role="img" aria-label="Photo of a happy charter client"></div>
    <div class="reviewer-name">Mike R., Happy Customer</div>
    <div class="dots"><span></span><span></span><span></span></div>
  </div>
</section>

<footer class="footer">
  <div class="col links">
    <h4>Quick <span>Links</span></h4>
    <ul>
      <li>Home</li><li>About</li><li>Pick Up Locations</li><li>Rates</li><li>Contact Us</li><li>Gift Card</li>
    </ul>
  </div>
  <div class="col badges">
    <h4>Customer <span>Reviews</span></h4>
    <div class="badge-row"><div class="badge"></div><div class="badge"></div></div>
  </div>
  <div class="col details">
    <h4>Contact <span>Details</span></h4>
    <div class="detail">
      <svg viewBox="0 0 24 24" aria-hidden="true"><path d="M12 2a7 7 0 0 0-7 7c0 5 7 13 7 13s7-8 7-13a7 7 0 0 0-7-7zm0 9.5A2.5 2.5 0 1 1 12 6a2.5 2.5 0 0 1 0 5.5z" fill="#3a8fe4"/></svg>
      <span>Fishing Charters<br>Harbor Point Marina, 12 Bayside Drive<br>Tampa, FL 33600, United States<br>Boat Pickup Available</span>
    </div>
    <div class="detail">
      <svg viewBox="0 0 24 24" aria-hidden="true"><path d="M6.6 10.8a15 15 0 0 0 6.6 6.6l2.2-2.2a1 1 0 0 1 1-.25 11.4 11.4 0 0 0 3.6.57 1 1 0 0 1 1 1V20a1 1 0 0 1-1 1A17 17 0 0 1 3 4a1 1 0 0 1 1-1h3.5a1 1 0 0 1 1 1c0 1.25.2 2.45.57 3.57a1 1 0 0 1-.25 1z" fill="#3a8fe4"/></svg>
      <span>555-014-2277</span>
    </div>
    <div class="detail">
      <svg viewBox="0 0 24 24" aria-hidden="true"><path d="M3 5h18v14H3z" fill="none" stroke="#3a8fe4" stroke-width="2"/><path d="M3 6l9 7 9-7" fill="none" stroke="#3a8fe4" stroke-width="2"/></svg>
      <span>captdale@example.com</span>
    </div>
  </div>
  <a class="brand" href="#"><span class="brand-dot"></span>Marlow</a>
</footer>
<div class="copyright">
  <span>Copyright © 2016 reelcoastcharters.example. All Rights Reserved.</span>
  <span class="follow">Follow Us <span class="ring" aria-label="Chatterly"></span></span>
</div>

</body>
</html>
```